Church needs an introductory/informative postcard

We are looking for a postcard that would introduce our church along with having our programing information. We need it to be in Spanish, I can provide the necessary translation. Please provide us with ideas for a tag line that invites people to come check us out. We can provide a bible scripture if necessary, but would like something short that projects interest and confidence. We have a logo that we would like incorporated.

Target Market(s)

Hispanic

Industry/Entity Type

Religious

Requirements
Must have
• Colorful to coordinate with our logo so it flows well
• Have an tag line that invites people to our church
Nice to have
• have a modern feel
• if needed we can provide some pictures of our building
Should not have
• Pictures of people

```html
<!DOCTYPE html>
<html lang="es">
<head>
<meta charset="utf-8">
<title>Alborada – Postcard</title>
<link href="https://fonts.googleapis.com/css2?family=Cinzel:wght@400;700;900&family=Questrial&family=Montserrat:wght@700&display=swap" rel="stylesheet">
<style>
  :root{
    --stage:#2e2e2e;
    --paper:#ffffff;
    --panel-light:#f4f4f4;
    --panel-dark:#e4e4e4;
    --ink:#151515;
    --accent-red:#d8431c;
    --accent-blue:#2aa7e0;
    --accent-purple:#5b2d8c;
    --green-light:#bfe8cf;
    --green-mid:#5fbf8d;
    --green-deep:#1f5c3a;
    --frame:#222222;
  }
  *{margin:0;padding:0;box-sizing:border-box}
  html,body{width:900px;height:1200px;overflow:hidden}
  body{background:var(--stage);position:relative;font-family:"Questrial",sans-serif;color:var(--ink)}

  .card{position:absolute;left:105px;width:690px;height:530px;overflow:hidden}
  .card--front{top:53px}
  .card--back{top:630px;background:var(--paper)}

  /* front */
  .front-photo{position:absolute;inset:0;
    background:
      radial-gradient(ellipse at 30% 55%, rgba(230,250,200,.75) 0%, rgba(230,250,200,0) 45%),
      linear-gradient(180deg, var(--green-light) 0%, #8fd6b0 40%, var(--green-mid) 62%, var(--green-deep) 100%);}
  .brand-name{font-family:"Cinzel",serif;font-weight:700;color:var(--accent-purple);letter-spacing:1px;position:absolute;text-align:center;line-height:1}
  .card--front .brand-name{left:0;right:0;top:122px;font-size:27px}
  .tagline{position:absolute;left:0;right:0;text-align:center;font-family:"Cinzel",serif;line-height:1}
  .tagline__lead{top:190px;font-size:42px;font-weight:400;color:var(--ink)}
  .tagline__main{top:236px;font-size:40px;font-weight:700;color:var(--accent-red)}
  .front-web{position:absolute;left:0;right:0;top:490px;display:flex;justify-content:center;align-items:center;gap:8px;color:#f2f2f2;font-size:19px}

  /* back: info panel with plain vertical edge bands */
  .info-panel{position:absolute;left:0;top:0;width:322px;height:463px;
    background:linear-gradient(90deg,var(--panel-light),var(--panel-dark))}
  .edge-band{position:absolute;top:0;height:463px}
  .edge-band--red{left:322px;width:10px;background:var(--accent-red)}
  .edge-band--blue{left:335px;width:7px;background:var(--accent-blue)}
  .edge-band--purple{left:345px;width:4px;background:var(--accent-purple)}

  .info{position:absolute;left:35px;top:0;width:285px}
  .info > *{position:absolute;left:0;white-space:nowrap;line-height:1}
  .info__question{top:24px;font-family:"Cinzel",serif;font-size:19px}
  .info__headline{top:51px;font-family:"Cinzel",serif;font-weight:900;font-size:23px}
  .info__rule{top:82px;width:270px;height:1px;background:var(--accent-blue)}
  .info__label{font-family:"Cinzel",serif;font-size:18px;color:var(--accent-red)}
  .info__label--strong{font-weight:900}
  .info__text{font-size:18px}
  .schedule{font-family:"Cinzel",serif;font-weight:900;font-size:13px}
  .schedule span{color:var(--accent-blue)}
  .info__phone{font-family:"Montserrat",sans-serif;font-weight:700;font-size:17px}
  .social{top:405px;left:103px !important;display:flex;gap:11px}
  .social i{display:block;width:18px;height:18px;background:var(--ink);border-radius:3px}
  .info__web{font-size:12.5px;color:var(--accent-blue)}

  .card--back .brand-name{left:400px;width:150px;top:89px;font-size:17px}
  .stamp-box{position:absolute;left:577px;top:29px;width:82px;height:86px;border:1px solid var(--frame)}
</style>
</head>
<body>

<section class="card card--front">
  <div class="front-photo" role="img" aria-label="Congregation worshipping with raised hands, backlit in soft green light"></div>
  <div class="brand-name">ALBORADA</div>
  <div class="tagline tagline__lead">Come</div>
  <div class="tagline tagline__main">WORSHIP WITH US.</div>
  <div class="front-web">
    <svg width="16" height="16" viewBox="0 0 16 16" fill="none" stroke="#f2f2f2" stroke-width="1.3">
      <circle cx="8" cy="8" r="6.5"/><ellipse cx="8" cy="8" rx="3" ry="6.5"/><path d="M1.5 8h13"/>
    </svg>
    <span>www.iglesiaalborada.org</span>
  </div>
</section>

<section class="card card--back">
  <div class="info-panel"></div>
  <div class="edge-band edge-band--red"></div>
  <div class="edge-band edge-band--blue"></div>
  <div class="edge-band edge-band--purple"></div>

  <div class="info">
    <div class="info__question">Where can God</div>
    <div class="info__headline">USE YOUR TALENTS?</div>
    <div class="info__rule"></div>
    <div class="info__label" style="top:99px">ENVÍANOS EMAIL</div>
    <div class="info__text" style="top:128px">info@iglesiaalborada.org</div>
    <div class="info__label" style="top:158px">LLÁMANOS</div>
    <div class="info__text" style="top:187px">2450 Cedar Bend Ave.</div>
    <div class="info__text" style="top:209px">Maple Springs, TX 75999</div>
    <div class="info__label info__label--strong" style="top:246px">Servicios:</div>
    <div class="schedule" style="top:274px">domingo <span>10:00 am</span></div>
    <div class="schedule" style="top:295px">lunes <span>7:00 pm</span></div>
    <div class="schedule" style="top:317px">miércoles <span>7:00 pm</span></div>
    <div class="info__label info__label--strong" style="top:353px">TELÉFONO:</div>
    <div class="info__phone" style="top:377px">555.014.2290</div>
    <div class="info__label" style="top:410px;font-size:14px">SÍGUENOS</div>
    <div class="social" aria-label="Redes sociales"><i></i><i></i><i></i></div>
    <div class="info__web" style="top:435px">www.iglesiaalborada.org</div>
  </div>

  <div class="brand-name">ALBORADA</div>
  <div class="stamp-box"></div>
</section>

</body>
</html>
```